Clever Burrow

Create effective banner ads for the website CleverBurrow.com. We are building a re-target ad for coffee shops and/or stay at home office workers, and we would like to order 3 separate designs with the banner sizes 300x250, 728x90, 320x50, 640x100, 300x50, and 160x600, and they all need to be under 40kb of data. We have provided 9 slogans you can use in the Banner Ad Slogans and Extra Details document. Feel free to create your own slogan, and use resources found on our website.

Industry/Entity Type

Building

```html
<!DOCTYPE html>
<html lang="en">
<head>
<meta charset="utf-8">
<title>Clever Burrow – Banner</title>
<link rel="stylesheet" href="https://fonts.googleapis.com/css2?family=Figtree:wght@400;500;700;800;900&display=swap">
<style>
  :root {
    --brand-blue: #1f4ea3;
    --deep-navy: #0b1a3d;
    --band-blue: #1a3c8c;
    --paper: #eeeff1;
    --ink: #3a3a3a;
    --white: #ffffff;
    --photo-dark: #1c1c1e;
    --photo-mid: #5a5a5c;
  }
  * { margin: 0; padding: 0; box-sizing: border-box; }
  html, body { width: 1200px; height: 1000px; overflow: hidden; background: var(--paper); }
  .banner {
    position: relative; width: 1200px; height: 1000px; overflow: hidden;
    font-family: "Figtree", "Helvetica Neue", Arial, sans-serif;
  }
  .banner-shapes { position: absolute; inset: 0; }
  .brand-badge {
    position: absolute; left: 55px; top: 40px; width: 262px; height: 262px;
    border-radius: 50%; background: var(--deep-navy);
    border: 5px solid var(--white);
    box-shadow: 0 0 0 14px var(--deep-navy);
    display: flex; flex-direction: column; align-items: center; justify-content: center;
    color: var(--white); text-align: center;
  }
  .brand-name { font-weight: 800; font-size: 30px; line-height: 1.05; letter-spacing: 0.5px; }
  .brand-tagline { font-weight: 400; font-size: 15px; margin-top: 8px; letter-spacing: 1px; }
  .headline { position: absolute; left: 0; top: 0; }
  .headline-line {
    position: absolute; background: var(--brand-blue); color: var(--white);
    font-weight: 700; font-size: 86px; line-height: 1; letter-spacing: -1px;
    padding: 6px 22px 14px 20px; white-space: nowrap; transform: rotate(-1deg);
  }
  .headline-line.line-1 { left: 80px; top: 472px; }
  .headline-line.line-2 { left: 28px; top: 585px; }
  .headline-line.line-3 { left: 42px; top: 700px; transform: rotate(1deg); }
  .subline {
    position: absolute; left: 60px; top: 842px;
    font-size: 36px; line-height: 43px; color: var(--ink); font-weight: 400;
  }
  .subline .brand-mention { color: var(--brand-blue); font-weight: 700; }
  .cta-button {
    position: absolute; left: 558px; top: 904px; width: 268px; height: 60px;
    border: 3px solid var(--white); border-radius: 8px;
    display: flex; align-items: center; justify-content: center;
    color: var(--brand-blue); font-weight: 900; font-size: 34px; letter-spacing: 0.5px;
  }
  .cta-note {
    position: absolute; right: 38px; top: 850px; text-align: right;
    color: var(--white); font-size: 31px; line-height: 38px; font-weight: 400;
  }
  .cta-note strong { font-weight: 700; }
</style>
</head>
<body>
<main class="banner">
  <svg class="banner-shapes" width="1200" height="1000" viewBox="0 0 1200 1000" aria-hidden="false">
    <defs>
      <linearGradient id="photoTone" x1="0" y1="0" x2="1" y2="1">
        <stop offset="0" stop-color="#3b3b3d"/>
        <stop offset="0.45" stop-color="var(--photo-mid)"/>
        <stop offset="1" stop-color="var(--photo-dark)"/>
      </linearGradient>
      <linearGradient id="bandTone" x1="0" y1="0" x2="0" y2="1">
        <stop offset="0" stop-color="#0e2560"/>
        <stop offset="0.5" stop-color="var(--band-blue)"/>
        <stop offset="1" stop-color="#10275e"/>
      </linearGradient>
    </defs>
    <rect class="photo-area" x="0" y="0" width="1200" height="1000" fill="url(#photoTone)" role="img"
          aria-label="Black and white photo of two men relaxing in lounge chairs in a coworking space, a car visible through a glass garage door"/>
    <polygon class="paper-panel" points="0,0 110,0 410,1000 0,1000" fill="var(--paper)"/>
    <polygon class="blue-band" points="110,0 330,0 560,1000 410,1000" fill="url(#bandTone)"/>
    <polygon class="corner-block" points="915,540 1070,490 1200,860 1200,1000 870,1000 845,820" fill="var(--brand-blue)"/>
    <line class="accent-line" x1="318" y1="272" x2="368" y2="425" stroke="var(--white)" stroke-width="2"/>
    <line class="accent-line" x1="846" y1="876" x2="870" y2="955" stroke="var(--white)" stroke-width="2"/>
    <line class="accent-line" x1="1025" y1="392" x2="1062" y2="485" stroke="var(--brand-blue)" stroke-width="4"/>
  </svg>

  <div class="brand-badge">
    <span class="brand-name">Clever<br>Burrow</span>
    <span class="brand-tagline">business incubator</span>
  </div>

  <h1 class="headline">
    <span class="headline-line line-1">Coffee</span>
    <span class="headline-line line-2">Shops are for</span>
    <span class="headline-line line-3">Socializing</span>
  </h1>

  <p class="subline">Get Real Work<br>Done at<br><span class="brand-mention">Clever Burrow</span></p>

  <a class="cta-button">CLICK HERE</a>

  <p class="cta-note">to schedule<br>a Tour and get a<br><strong>Free Day Pass</strong></p>
</main>
</body>
</html>
```